Northgate Signal Shield LLC

Need help designing a web page for an alarm company. I want to promote my business.

Target Market(s)

Residential and commercial clients

Industry/Entity Type

Security Service

Coding

Coded - Design and coding required

Number of Pages Required

2 page

Font styles to use
Sans Serif

Requirements
Must have
• I would llike my logo displayed on the page. I would like my slogan displayed as well
´´A GREAT PLACE FOR YOUR SECURITY NEEDS´´
We are licensed and insured
Company phone number 713-555-0142
Company hours: Monday-Friday 8am-5pm Company address: P.O. Box 419 Crosby, TX 77064 over 25 years experience
Email info. Northgatess@ferntopmail.com
Company license #K52948316
Fire license# TMV-6614027
JLP-8170326
We offer alarm monitoring,security cameras, access control,gate openers, home theater systems, covert camera installations, FIre alarm installation and monitoring
Nice to have
• We offer security at competitive prices.
Get customer information for a free quote similar to brx website.
Should not have
• No prices listed on website

```html
<!DOCTYPE html>
<html lang="en">
<head>
<meta charset="utf-8">
<title>Northgate Signal Shield LLC</title>
<link href="https://fonts.googleapis.com/css2?family=Montserrat:wght@400;500;600;700&family=Roboto:wght@400;500;700&display=swap" rel="stylesheet">
<style>
:root{
  --red:#e1251b;
  --red-dark:#b5140e;
  --ink:#1b1b1b;
  --body:#555;
  --muted:#8a8a8a;
  --line:#cfcfcf;
  --light:#f4f4f4;
  --footer:#151515;
  --white:#fff;
}
*{margin:0;padding:0;box-sizing:border-box}
html,body{width:1200px;height:4839px;overflow:hidden}
body{position:relative;background:var(--white);font-family:"Roboto",Arial,sans-serif;color:var(--ink)}
.abs{position:absolute}
.label{font-family:"Montserrat",Arial,sans-serif;font-weight:500;color:var(--red);letter-spacing:2px;font-size:16px;text-transform:uppercase}
.title{font-family:"Roboto",Arial,sans-serif;font-weight:700;color:var(--ink);font-size:36px}
.center{left:0;width:1200px;text-align:center}
.mark{width:62px;height:62px;border-radius:50%;background:var(--red);left:569px}
.btn{display:flex;align-items:center;justify-content:center;background:var(--red);color:var(--white);font-family:"Montserrat",Arial,sans-serif;font-weight:700;font-size:14px;text-transform:uppercase;letter-spacing:.5px}
.para{font-size:12.5px;line-height:27px;color:var(--body)}

/* header */
.header{top:0;left:0;width:1200px;height:107px;background:var(--white)}
.phone{top:16px;left:111px;font-size:17px;font-weight:500;display:flex;align-items:center;gap:12px}
.nav a{position:absolute;top:64px;font-family:"Montserrat",Arial,sans-serif;font-weight:600;font-size:15.5px;color:var(--ink);text-decoration:none}
.nav a.active{color:var(--red)}
.quote-top{top:11px;left:954px;width:132px;height:40px;border:2px solid var(--red);color:var(--red);font-family:"Montserrat",Arial,sans-serif;font-weight:600;font-size:14px;display:flex;align-items:center;justify-content:center}
.logo-tab{top:0;left:480px;width:240px;height:148px;background:var(--white);border-radius:0 0 40px 40px;display:flex;flex-direction:column;align-items:center;justify-content:center;gap:6px;z-index:3}
.logo-tab .dot{width:50px;height:50px;border-radius:50%;background:var(--red)}
.logo-name{font-family:"Roboto",Arial,sans-serif;font-weight:700;color:var(--red);font-size:34px;letter-spacing:1px}

/* hero */
.hero{top:107px;left:0;width:1200px;height:630px;background:linear-gradient(110deg,#0a1a44 0%,#123a86 45%,#2f6fc8 70%,#0e2c6c 100%)}
.hero-eyebrow{top:300px;left:131px;font-family:"Montserrat",Arial,sans-serif;font-weight:500;color:var(--red);font-size:30px;letter-spacing:1px}
.hero-head{top:344px;left:131px;color:var(--white);font-weight:700;font-size:47px;line-height:60px;font-family:"Roboto",Arial,sans-serif}
.hero-btn{top:483px;left:131px;width:160px;height:49px}
.arrow-c{width:42px;height:42px;border:2px solid var(--white);border-radius:50%;display:flex;align-items:center;justify-content:center}

/* services */
.card{width:237px;height:269px}
.card .cap{position:absolute;left:0;bottom:22px;width:100%;text-align:center;color:var(--white);font-weight:500;font-size:16px}

/* about */
.about-text{top:1436px;left:670px;width:420px}

/* testimonials */
.testi{top:1825px;left:0;width:1200px;height:560px;background:linear-gradient(180deg,#2b2f5a 0%,#3d3150 45%,#1d2030 75%,#14161f 100%)}
.tcard{top:2073px;width:312px;height:222px;background:var(--white);padding:24px 24px}
.tq{color:var(--red);font-size:48px;font-weight:700;line-height:34px;font-family:Georgia,serif}
.tbody{font-style:italic;font-size:14.5px;line-height:26px;color:#666;margin-top:8px;text-align:justify}
.tauthor{display:flex;align-items:center;gap:10px;margin-top:16px;font-size:15px;color:var(--ink)}
.avatar{width:44px;height:44px;border-radius:50%;background:#6b6b6b}

/* contact */
.field{height:47px;border:1px solid var(--line);border-radius:3px;font-size:12.5px;color:#777;display:flex;align-items:center;padding-left:24px}
.disclaim{font-size:9.5px;line-height:20.5px;color:#444}

/* partners */
.partners{top:2892px;left:0;width:1200px;height:197px;background:var(--light)}
.partner{top:2970px;display:flex;align-items:center;gap:10px;color:#5b5b5b;font-weight:700;font-size:22px;font-family:"Roboto",Arial,sans-serif}
.pshape{width:36px;height:36px;background:#5b5b5b;border-radius:50%}

/* cta */
.cta{top:3089px;left:0;width:1200px;height:329px;background:linear-gradient(135deg,#d8221c 0%,#e33a2c 40%,#c61712 100%)}

/* news */
.news{width:306px}
.news .img{height:201px}
.news h3{font-size:17px;font-weight:500;line-height:30px;margin-top:17px;color:var(--ink)}
.news p{font-size:10.5px;line-height:23px;color:#555;margin-top:4px}
.news .more{display:inline-block;margin-top:12px;font-weight:700;font-size:15px;color:var(--ink);padding-bottom:6px;border-bottom:3px solid var(--red)}

/* footer */
.footer{top:4441px;left:0;width:1200px;height:329px;background:var(--footer)}
.fhead{font-family:"Montserrat",Arial,sans-serif;font-weight:600;font-size:14px;color:var(--white)}
.flinks{font-size:13px;line-height:28.5px;color:var(--white)}
.ftext{font-size:13px;line-height:23px;color:var(--white)}
.social{width:32px;height:32px;border-radius:50%;background:var(--white)}
.bottom{top:4770px;left:0;width:1200px;height:69px;background:#0c0c0c;color:var(--white);font-size:13px}
</style>
</head>
<body>

<!-- header -->
<header class="abs header">
  <div class="abs phone">
    <svg width="20" height="20" viewBox="0 0 24 24"><path d="M6.6 10.8a15.1 15.1 0 0 0 6.6 6.6l2.2-2.2c.3-.3.7-.4 1-.2 1.1.4 2.3.6 3.6.6.6 0 1 .4 1 1V20c0 .6-.4 1-1 1A17 17 0 0 1 3 4c0-.6.4-1 1-1h3.5c.6 0 1 .4 1 1 0 1.3.2 2.5.6 3.6.1.3 0 .7-.2 1z" fill="#1b1b1b"/></svg>
    713-555-0142
  </div>
  <nav class="nav">
    <a class="active" style="left:111px">HOME</a>
    <a style="left:231px">ABOUT US</a>
    <a style="left:388px">SERVICES</a>
    <a style="left:734px">PROJECTS</a>
    <a style="left:884px">BLOG</a>
    <a style="left:1005px">CONTACT</a>
  </nav>
  <div class="abs quote-top">GET A QUOTE</div>
</header>
<div class="abs logo-tab">
  <div class="dot"></div>
  <div class="logo-name">NORTHGATE</div>
</div>

<!-- hero -->
<section class="abs hero" role="img" aria-label="Close-up of a white security camera over a glowing blue network background"></section>
<svg class="abs" style="top:620px;left:0" width="1200" height="120" viewBox="0 0 1200 120" aria-hidden="true">
  <path d="M0 115 Q600 110 1200 20 L1200 120 L0 120Z" fill="#fff"/>
  <path d="M0 108 Q600 104 1200 12" stroke="#e1251b" stroke-width="4" fill="none"/>
</svg>
<div class="abs hero-eyebrow">NORTHGATE</div>
<h1 class="abs hero-head">A GREAT PLACE FOR<br>YOUR SECURITY NEEDS</h1>
<div class="abs btn hero-btn">GET STARTED</div>
<div class="abs arrow-c" style="top:396px;left:46px"><svg width="12" height="18" viewBox="0 0 12 18"><path d="M10 2 3 9l7 7" stroke="#fff" stroke-width="2" fill="none"/></svg></div>
<div class="abs arrow-c" style="top:396px;left:1111px"><svg width="12" height="18" viewBox="0 0 12 18"><path d="M2 2l7 7-7 7" stroke="#fff" stroke-width="2" fill="none"/></svg></div>

<!-- services -->
<div class="abs mark" style="top:755px"></div>
<div class="abs label center" style="top:826px">SERVICES</div>
<h2 class="abs title center" style="top:855px">What We Offer</h2>
<svg class="abs" style="top:1075px;left:82px" width="12" height="20" viewBox="0 0 12 20"><path d="M10 2 3 10l7 8" stroke="#333" stroke-width="2" fill="none"/></svg>
<svg class="abs" style="top:1075px;left:1106px" width="12" height="20" viewBox="0 0 12 20"><path d="M2 2l7 8-7 8" stroke="#333" stroke-width="2" fill="none"/></svg>
<div class="abs card" style="top:966px;left:111px;background:linear-gradient(135deg,#4d5f78,#1f2b3f)" role="img" aria-label="Security guard watching a wall of monitors"><span class="cap">ALARM MONITORING</span></div>
<div class="abs card" style="top:937px;left:359px;background:linear-gradient(135deg,#7a1820,#2a0d14)" role="img" aria-label="Dome camera lens glowing red"><span class="cap">SECURITY CAMERAS</span></div>
<div class="abs card" style="top:966px;left:605px;background:linear-gradient(135deg,#b9c2bf,#6f7a76)" role="img" aria-label="Finger pressing an access control keypad"><span class="cap">ACCESS CONTROL</span></div>
<div class="abs card" style="top:937px;left:851px;background:linear-gradient(135deg,#e2261f,#8f110c)" role="img" aria-label="Television and speakers in a red home theater room"><span class="cap">HOME THEATER SYSTEMS</span></div>

<!-- about -->
<svg class="abs" style="top:1339px;left:0" width="620" height="486" viewBox="0 0 620 486" role="img" aria-label="Technician installing a fingerprint access reader on a brick wall">
  <defs><linearGradient id="aboutFill" x1="0" x2="1"><stop offset="0" stop-color="#8a4a38"/><stop offset=".45" stop-color="#c9c2ba"/><stop offset="1" stop-color="#e8e4e0"/></linearGradient></defs>
  <path d="M0 0H540Q640 240 560 486H0Z" fill="url(#aboutFill)"/>
  <path d="M540 0Q640 240 560 486" stroke="#e1251b" stroke-width="4" fill="none"/>
</svg>
<div class="abs about-text">
  <div class="label" style="font-size:15px">ABOUT COMPANY</div>
  <h2 style="font-size:26px;font-weight:700;margin-top:12px">Northgate Signal Shield LLC</h2>
  <p class="para" style="margin-top:18px">Lorem ipsum dolor sit amet, consecte piscing elit, sed do eiusmod tempor incididunt ut labore et dolore ma ndisse ultrices ravida. Ri ommodo viverra maecenas accumsan lacus vel facilisem ipsum dolor sit amet, consectetur adipiscing elit, sed do eiusmod tempor incididunt et dolore magna aliqua. Quis ipsum suspendisse ultrices gravida.</p>
  <div class="btn" style="width:160px;height:49px;margin-top:26px">LEARN MORE</div>
</div>

<!-- testimonials -->
<section class="abs testi" role="img" aria-label="City skyline at night with a dome security camera"></section>
<div class="abs mark" style="top:1908px"></div>
<div class="abs label center" style="top:1981px">TESTIMONIALS</div>
<h2 class="abs title center" style="top:2004px;color:#fff">What Our Client says</h2>
<div class="abs tcard" style="left:111px"><div class="tq">“</div><p class="tbody">Lorem ipsum dolor sit t, consectetur adipiscing elit, sed do eiusmod tempor incididunt ut labore et</p><div class="tauthor"><div class="avatar" role="img" aria-label="Client portrait"></div>- Daniel Reyes</div></div>
<div class="abs tcard" style="left:443px"><div class="tq">“</div><p class="tbody">Lorem ipsum dolor sit t, consectetur adipiscing elit, sed do eiusmod tempor incididunt ut labore et</p><div class="tauthor"><div class="avatar" role="img" aria-label="Client portrait"></div>- Daniel Reyes</div></div>
<div class="abs tcard" style="left:776px"><div class="tq">“</div><p class="tbody">Lorem ipsum dolor sit t, consectetur adipiscing elit, sed do eiusmod tempor incididunt ut labore et</p><div class="tauthor"><div class="avatar" role="img" aria-label="Client portrait"></div>- Daniel Reyes</div></div>

<!-- contact -->
<div class="abs mark" style="top:2466px;left:111px"></div>
<div class="abs label" style="top:2539px;left:111px">CONTACT US</div>
<h2 class="abs" style="top:2570px;left:111px;font-size:35px;font-weight:500;line-height:46px">Get a free quote<br>and audio&nbsp; voice security</h2>
<p class="abs para" style="top:2703px;left:113px;width:400px">Ready to customize an Northgate plan that works for you? Give us a call at (713-555-0142 to talk to an Northgate Specialist today — or fill out the form to have us contact you.</p>
<div class="abs field" style="top:2470px;left:655px;width:393px">Name</div>
<div class="abs field" style="top:2535px;left:655px;width:393px">Email</div>
<div class="abs field" style="top:2603px;left:655px;width:230px">Phone</div>
<div class="abs field" style="top:2603px;left:899px;width:149px">ZIP</div>
<p class="abs disclaim" style="top:2667px;left:655px;width:420px">By clicking the 'Get a Free Quote' button below, I agree that an NORTHGATE specialist may contact me via text messages or phone calls to the phone number provided by me using automated technology about brx offers and consent is not required to make a purchase. Your information is collected and used in accordance with our privacy policy.</p>
<div class="abs btn" style="top:2761px;left:655px;width:172px;height:47px">GET A FREE QUOTE</div>

<!-- partners -->
<section class="abs partners"></section>
<svg class="abs" style="top:2980px;left:82px" width="12" height="20" viewBox="0 0 12 20"><path d="M10 2 3 10l7 8" stroke="#333" stroke-width="2" fill="none"/></svg>
<svg class="abs" style="top:2980px;left:1106px" width="12" height="20" viewBox="0 0 12 20"><path d="M2 2l7 8-7 8" stroke="#333" stroke-width="2" fill="none"/></svg>
<div class="abs partner" style="left:116px"><span class="pshape"></span>Brightpath</div>
<div class="abs partner" style="left:316px;font-size:17px"><span class="pshape" style="border-radius:0"></span>DUMMY LOGO</div>
<div class="abs partner" style="left:540px;font-size:17px"><span class="pshape"></span>Veranda Labs</div>
<div class="abs partner" style="left:712px;font-size:15px"><span class="pshape"></span>KEYSTONE WORKS</div>
<div class="abs partner" style="left:892px"><span class="pshape" style="border-radius:0"></span>PLACEHOLDER</div>

<!-- cta -->
<section class="abs cta" role="img" aria-label="Person working at a laptop with a red overlay"></section>
<h2 class="abs center" style="top:3175px;color:#fff;font-size:25px;font-weight:700">DELIVERING THE BEST SECURITY SOLUTIONS TO OUR CLIENTS</h2>
<p class="abs center" style="top:3222px;color:#fff;font-size:12px;line-height:24px;padding:0 230px">Lorem ipsum dolor sit amet, consectetur adipiscing elit, sed do eiusmod tempor incididunt ut labore et dolore magna aliqua. Quis ipsum suspendisse ultrices gravida. Risus commodo viverra maecenas accumsan lacus vel facilisis.</p>
<div class="abs" style="top:3283px;left:513px;width:174px;height:49px;border:2px solid #fff;color:#fff;display:flex;align-items:center;justify-content:center;font-size:14px;font-weight:500">GET A FREE QUOTE</div>

<!-- news -->
<div class="abs mark" style="top:3490px"></div>
<div class="abs label center" style="top:3559px">NEWS UPDATES</div>
<h2 class="abs title center" style="top:3589px">Latest News</h2>
<article class="abs news" style="top:3653px;left:111px"><div class="img" style="background:linear-gradient(135deg,#9aa3a8,#4f5659)" role="img" aria-label="Security turnstile gates in a lobby"></div><h3>Lorem ipsum dolor sit tetur adipiscing elit, sed do eiusmod tempor</h3><p>Lorem ipsum dolor sit amet, consectetur adipiscing elit, sed do eiusmod tempor incididunt</p><span class="more">READ MORE</span></article>
<article class="abs news" style="top:3653px;left:446px"><div class="img" style="background:linear-gradient(135deg,#d9d4cc,#c2371f)" role="img" aria-label="Technician in a hard hat installing a camera"></div><h3>Lorem ipsum dolor sit tetur adipiscing elit, sed do eiusmod tempor</h3><p>Lorem ipsum dolor sit amet, consectetur adipiscing elit, sed do eiusmod tempor incididunt</p><span class="more">READ MORE</span></article>
<article class="abs news" style="top:3653px;left:781px"><div class="img" style="background:linear-gradient(135deg,#4d5a55,#e7e7e4)" role="img" aria-label="Hand using an alarm keypad on a wall"></div><h3>Lorem ipsum dolor sit tetur adipiscing elit, sed do eiusmod tempor</h3><p>Lorem ipsum dolor sit amet, consectetur adipiscing elit, sed do eiusmod tempor incididunt</p><span class="more">READ MORE</span></article>

<!-- skyline -->
<div class="abs" style="top:4040px;left:0;width:1200px;height:402px;background:linear-gradient(180deg,#ffffff 0%,#9a9a9a 45%,#151515 100%)" role="img" aria-label="Black city skyline silhouette"></div>

<!-- footer -->
<footer class="abs footer">
  <div class="abs" style="top:40px;left:111px;width:230px;display:flex;flex-direction:column;align-items:center;gap:8px">
    <div style="width:50px;height:50px;border-radius:50%;background:var(--red)"></div>
    <div class="logo-name" style="font-size:36px">NORTHGATE</div>
  </div>
  <div class="abs ftext" style="top:244px;left:113px;font-size:12.5px;line-height:26px">COMPANY LICENSE #K52948316<br>FIRE LICENSE# TMV-6614027<br>JLP-8170326</div>

  <div class="abs fhead" style="top:55px;left:393px">QUICK LINKS</div>
  <div class="abs flinks" style="top:100px;left:393px">Home<br>About<br>Our Services<br>Recent Projects<br>Testimonials<br>Blog<br>Contact</div>

  <div class="abs fhead" style="top:55px;left:561px">CONTACT US</div>
  <svg class="abs" style="top:108px;left:566px" width="22" height="22" viewBox="0 0 22 22"><circle cx="11" cy="11" r="11" fill="#333"/><path d="M11 5a4 4 0 0 0-4 4c0 3 4 8 4 8s4-5 4-8a4 4 0 0 0-4-4z" fill="#fff"/></svg>
  <div class="abs ftext" style="top:102px;left:597px">1234 Lorem ipsum sed<br>xxxx United States 0000</div>
  <svg class="abs" style="top:168px;left:566px" width="22" height="22" viewBox="0 0 22 22"><circle cx="11" cy="11" r="11" fill="#333"/><path d="M8 6l2 3-1 1a6 6 0 0 0 3 3l1-1 3 2-1 2c-4 0-9-5-9-9z" fill="#fff"/></svg>
  <div class="abs ftext" style="top:168px;left:597px">713-555-0142</div>
  <svg class="abs" style="top:212px;left:566px" width="22" height="22" viewBox="0 0 22 22"><circle cx="11" cy="11" r="11" fill="#333"/><rect x="6" y="7" width="10" height="8" fill="none" stroke="#fff"/><path d="M6 7l5 4 5-4" stroke="#fff" fill="none"/></svg>
  <div class="abs ftext" style="top:212px;left:597px">Northgatess@ferntopmail.com</div>

  <div class="abs fhead" style="top:55px;left:824px">SUBSCRIBE TO OUR BLOG</div>
  <div class="abs ftext" style="top:96px;left:824px;width:280px;line-height:28px">Sign up today to get resources on how to attract and retain more customers!</div>
  <div class="abs" style="top:173px;left:824px;width:263px;height:47px;background:#fff;border-radius:24px;display:flex;align-items:center;padding-left:20px;font-size:12.5px;color:#777">✉&nbsp; Email Address</div>
  <div class="abs" style="top:173px;left:1038px;width:49px;height:47px;background:var(--red);border-radius:0 24px 24px 0;display:flex;align-items:center;justify-content:center"><svg width="16" height="16" viewBox="0 0 16 16"><path d="M1 8l14-7-5 14-2-6z" fill="#fff"/></svg></div>
  <div class="abs social" style="top:242px;left:827px"></div>
  <div class="abs social" style="top:242px;left:865px"></div>
  <div class="abs social" style="top:242px;left:902px"></div>
  <div class="abs social" style="top:242px;left:940px"></div>
</footer>
<div class="abs bottom">
  <div class="abs" style="top:24px;left:111px">Copyright © 2020. <span style="color:var(--red);text-decoration:underline">Northgate Signal Shield LLC</span> All Rights Reserved</div>
  <div class="abs" style="top:24px;left:816px">Terms and Conditions &nbsp;|&nbsp; Privacy Policy</div>
</div>

</body>
</html>
```